QR TILL WORKS , CREDIT CARD PROCESSING EQUIPMENT

qrtillworks is a sub division of Tallow a credit car processing co.
harold finch
14 cedar hollow ln
fernhaven oh 07312
suite 412

qrtillworks.example
cell 555-214-7730
office 555-861-2093
we sell pos systems to merchant who want to accept credit cards at there retail location.
black card would be nice buit open to different ideas

Target Market(s)

retail merchants

Industry/Entity Type

credit card processing

Contact Information for Business Card

card should include web site phone address

Colors

Designer to choose colors to be used in the design.

Requirements
Should not have
• red

```html
<!DOCTYPE html>
<html lang="en">
<head>
<meta charset="utf-8">
<title>QR TILL WORKS – Business Card</title>
<link href="https://fonts.googleapis.com/css2?family=Montserrat:wght@500;700&display=swap" rel="stylesheet">
<style>
  :root{
    --backdrop:#2b2b2d;
    --card:#121212;
    --accent:#f2c511;
    --ink:#f4f4f4;
    --muted:#c9c9c9;
    --rule:#3a3a3a;
  }
  *{box-sizing:border-box;margin:0;padding:0}
  html,body{width:1200px;height:1015px;overflow:hidden}
  body{
    background:var(--backdrop);
    font-family:"Montserrat",Arial,sans-serif;
    position:relative;
  }
  .card{
    position:absolute;
    left:290px;
    width:620px;
    height:354px;
    background:var(--card);
    border-radius:30px;
    overflow:hidden;
    box-shadow:0 18px 40px rgba(0,0,0,.45);
  }
  .card::after{
    content:"";
    position:absolute;left:0;right:0;bottom:0;
    height:12px;
    background:var(--accent);
  }
  .card--front{top:110px}
  .card--back{top:540px}

  .brand{
    display:flex;align-items:center;gap:12px;
    color:var(--ink);
    font-weight:700;
    letter-spacing:.04em;
    white-space:nowrap;
  }
  .brand__dot{
    width:14px;height:14px;border-radius:50%;
    background:var(--accent);
    flex:none;
  }
  .card--front .brand{
    position:absolute;left:0;right:0;top:0;bottom:12px;
    justify-content:center;
    font-size:44px;
  }
  .card--back .brand{
    position:absolute;left:34px;top:212px;
    font-size:25px;
  }
  .divider{
    position:absolute;left:330px;top:40px;
    width:1px;height:240px;
    background:linear-gradient(to bottom,transparent,var(--rule) 25%,var(--rule) 75%,transparent);
  }
  .contact{
    position:absolute;left:362px;top:66px;
    color:var(--muted);
    font-weight:500;
    font-size:15px;
    line-height:1.55;
  }
  .contact__name{
    color:var(--accent);
    font-weight:700;
    font-size:25px;
    margin-bottom:12px;
    white-space:nowrap;
  }
  .contact__row{display:flex;align-items:center;gap:10px;white-space:nowrap;color:var(--ink)}
  .contact__row svg{width:15px;height:15px;flex:none}
  .contact__web .hl{color:var(--accent)}
  .contact__address{margin-top:12px;padding-left:25px;white-space:nowrap}
</style>
</head>
<body>

<section class="card card--front">
  <div class="brand"><span class="brand__dot"></span>QR TILL WORKS</div>
</section>

<section class="card card--back">
  <div class="brand"><span class="brand__dot"></span>QR TILL WORKS</div>
  <div class="divider"></div>
  <div class="contact">
    <div class="contact__name">Dorian Kessler</div>
    <div class="contact__row">
      <svg viewBox="0 0 16 16" fill="none" stroke="#f2c511" stroke-width="1.6"><rect x="2" y="3" width="12" height="10" rx="1.5"/><line x1="5" y1="11" x2="11" y2="11"/></svg>
      555-214-7730
    </div>
    <div class="contact__row">
      <svg viewBox="0 0 16 16" fill="#f2c511"><path d="M4 1.5l2.2 2.6-1.3 1.7a9 9 0 0 0 5.3 5.3l1.7-1.3 2.6 2.2-1.6 2.2C7.5 14 2 8.5 1.8 3.1z"/></svg>
      555-861-2093
    </div>
    <div class="contact__row contact__web">
      <svg viewBox="0 0 16 16" fill="none" stroke="#f2c511" stroke-width="1.3"><circle cx="8" cy="8" r="6.5"/><ellipse cx="8" cy="8" rx="2.8" ry="6.5"/><line x1="1.5" y1="8" x2="14.5" y2="8"/><line x1="2.6" y1="4.6" x2="13.4" y2="4.6"/><line x1="2.6" y1="11.4" x2="13.4" y2="11.4"/></svg>
      <span>www.<span class="hl">qrtillworks</span>.example</span>
    </div>
    <div class="contact__address">
      14 cedar hollow ln<br>
      fernhaven oh 07312, suite 412
    </div>
  </div>
</section>

</body>
</html>
```